Dorsey K. Whitfield Business Card

We need a business card for our company Dorsey K. Whitfield Heating & Plumbing to be distributed to potential customers. It should follow the color scheme of our logo and have a modern upscale and masculine look.

The logo is attached and the info below should also be included:

5187 W. Quarry Bend Rd.
Corliss Mill, PA 17622

Tobias R. Whitfield
(717) 593-8126
tobiasreedwhitfield@mailvane.com
dorseykwhitfield.com
PA #038419

Industry/Entity Type

Business

Contact Information for Business Card

5187 W. Quarry Bend Rd.
Corliss Mill, PA 17622

Tobias R. Whitfield
(717) 593-8126
tobiasreedwhitfield@mailvane.com
dorseykwhitfield.com
PA #038419

Colors

Designer to choose colors to be used in the design.

Requirements
Must have
• Information above included

```html
<!DOCTYPE html>
<html lang="en">
<head>
<meta charset="utf-8">
<title>Dorsey K. Whitfield Heating &amp; Plumbing – Business Card</title>
<link rel="stylesheet" href="https://fonts.googleapis.com/css2?family=Michroma&family=Lato:wght@700;900&display=swap">
<style>
  :root {
    --stage: #111111;
    --card-dark: #0c0c0c;
    --card-light: #ffffff;
    --brand-blue: #1f5fb4;
    --brand-lime: #a8d13a;
    --ink: #141414;
  }
  * { box-sizing: border-box; margin: 0; padding: 0; }
  html, body { width: 1200px; height: 1000px; overflow: hidden; }
  body {
    background: var(--stage);
    display: flex;
    align-items: center;
    justify-content: center;
    gap: 60px;
    font-family: "Lato", sans-serif;
  }
  .card {
    width: 525px;
    height: 300px;
    border-radius: 22px;
    position: relative;
    overflow: hidden;
    box-shadow: 0 18px 40px rgba(0,0,0,.6);
  }
  /* Front */
  .card--front {
    background: var(--card-dark);
    display: flex;
    align-items: center;
    justify-content: center;
  }
  .brand-lockup {
    display: flex;
    align-items: center;
    gap: 18px;
  }
  .brand-square {
    width: 72px; height: 72px;
    background: var(--brand-blue);
    flex: none;
  }
  .brand-name {
    font-family: "Michroma", sans-serif;
    color: var(--brand-blue);
    font-size: 21px;
    line-height: 1.35;
    text-transform: uppercase;
  }
  /* Back */
  .card--back {
    background: var(--card-light);
    display: flex;
    align-items: center;
    padding: 0 24px 40px 34px;
    gap: 24px;
  }
  .card--back::after {
    content: "";
    position: absolute;
    left: 0; right: 0; bottom: 0;
    height: 40px;
    background: var(--brand-lime);
  }
  .mark {
    width: 130px;
    display: flex;
    flex-direction: column;
    align-items: center;
    gap: 10px;
    flex: none;
  }
  .mark__square { width: 110px; height: 110px; background: var(--brand-blue); }
  .mark__name {
    font-weight: 900;
    font-size: 13px;
    color: var(--brand-blue);
    text-align: center;
    line-height: 1.2;
  }
  .contact { color: var(--ink); font-weight: 700; font-size: 14px; line-height: 1.4; }
  .contact__name {
    font-family: "Michroma", sans-serif;
    font-size: 15px;
    color: var(--brand-blue);
    text-transform: uppercase;
    margin-bottom: 6px;
    white-space: nowrap;
  }
  .contact__name .surname { color: var(--brand-lime); }
  .contact__license {
    font-family: "Michroma", sans-serif;
    color: var(--brand-blue);
    font-size: 14px;
    margin: 6px 0 6px;
  }
  .contact__row { display: flex; align-items: center; gap: 8px; white-space: nowrap; }
  .contact__row svg { width: 13px; height: 13px; fill: var(--brand-blue); flex: none; }
</style>
</head>
<body>
  <section class="card card--front" aria-label="Card front">
    <div class="brand-lockup">
      <div class="brand-square"></div>
      <div class="brand-name">Dorsey K. Whitfield<br>Heating &amp; Plumbing</div>
    </div>
  </section>

  <section class="card card--back" aria-label="Card back">
    <div class="mark">
      <div class="mark__square"></div>
      <div class="mark__name">Dorsey K. Whitfield</div>
    </div>
    <div class="contact">
      <div class="contact__name">Tobias R. <span class="surname">Whitfield</span></div>
      <div>5187 W. Quarry Bend Rd.</div>
      <div>Corliss Mill, PA 17622</div>
      <div class="contact__license">PA #038419</div>
      <div class="contact__row">
        <svg viewBox="0 0 24 24"><path d="M6.6 10.8a15.1 15.1 0 0 0 6.6 6.6l2.2-2.2a1 1 0 0 1 1-.25 11.4 11.4 0 0 0 3.6.57 1 1 0 0 1 1 1V20a1 1 0 0 1-1 1A17 17 0 0 1 3 4a1 1 0 0 1 1-1h3.5a1 1 0 0 1 1 1c0 1.25.2 2.45.57 3.57a1 1 0 0 1-.25 1z"/></svg>
        <span>(717) 593-8126</span>
      </div>
      <div class="contact__row">
        <svg viewBox="0 0 24 24"><path d="M2 5h20v14H2z"/><path d="M2 5l10 8 10-8z" fill="#fff"/></svg>
        <span>tobiasreedwhitfield@mailvane.com</span>
      </div>
      <div class="contact__row">
        <svg viewBox="0 0 24 24"><path d="M12 2a10 10 0 1 0 0 20 10 10 0 0 0 0-20zm6.9 9h-3a15 15 0 0 0-1.3-6A8 8 0 0 1 18.9 11zM12 4c.9 1.2 1.8 3.6 2 7h-4c.2-3.4 1.1-5.8 2-7zM9.4 5a15 15 0 0 0-1.3 6h-3A8 8 0 0 1 9.4 5zM5.1 13h3a15 15 0 0 0 1.3 6 8 8 0 0 1-4.3-6zM12 20c-.9-1.2-1.8-3.6-2-7h4c-.2 3.4-1.1 5.8-2 7zm2.6-1a15 15 0 0 0 1.3-6h3a8 8 0 0 1-4.3 6z"/></svg>
        <span>dorseykwhitfield.com</span>
      </div>
    </div>
  </section>
</body>
</html>
```